Wedding location search & compare

We need a web design for a website (mobile & pc) which allows for searching and comparing of wedding locations. The design should be clean, stylish and original and it should have the following functionality:
- a search function (with summary overview and map view)
- a comparing function
- detail page per location
- review possibility
- login for storing favorites and show own history
- social function (liking, sharing, send to and cavorting)
- ad placement
- contact form

We also require a Logo Design. Please submit your ideas for that project here: Logo Design needed for web design project.

```html
<!DOCTYPE html>
<html lang="en">
<head>
<meta charset="utf-8">
<title>Wedding Location Search &amp; Compare</title>
<link rel="stylesheet" href="https://fonts.googleapis.com/css2?family=Roboto:wght@300;400;500&display=swap">
<style>
  :root {
    --plum: #8b2487;
    --plum-dark: #741c70;
    --plum-soft: #a24a9e;
    --map-base: #e9e5dc;
    --map-tone: #dcd7cc;
    --panel-bg: #ececec;
    --card-bg: #ffffff;
    --placeholder: #e6e6e6;
    --ink: #333333;
    --muted: #8a8a8a;
    --orange: #f39a1e;
    --band: rgba(110, 112, 122, 0.55);
    --white: #ffffff;
  }
  * { box-sizing: border-box; margin: 0; padding: 0; }
  html, body { width: 1200px; height: 800px; overflow: hidden; }
  body { font-family: "Roboto", sans-serif; color: var(--ink); background: var(--map-base); position: relative; }

  .topbar {
    position: absolute; left: 0; top: 0; width: 1200px; height: 46px;
    background: var(--plum); display: flex; align-items: center; padding: 0 70px; color: var(--white);
    font-size: 15px; font-weight: 300; z-index: 5;
  }
  .topbar nav a { color: var(--white); text-decoration: none; margin-right: 24px; }
  .topbar .divider { width: 1px; height: 24px; background: rgba(255,255,255,.6); margin: 0 14px 0 0; }
  .login input {
    height: 26px; border: none; background: var(--white); font-family: inherit; font-size: 12px;
    color: #888; padding: 0 8px; margin-right: 8px;
  }
  .login .email { width: 205px; }
  .login .password { width: 160px; }
  .topbar .help { margin-left: auto; }
  .topbar .help a { color: var(--white); text-decoration: none; margin-left: 42px; }

  .map {
    position: absolute; left: 0; top: 46px; width: 1200px; height: 754px;
    background: linear-gradient(135deg, var(--map-base) 0%, var(--map-tone) 55%, #c9d3dc 100%);
  }

  .pin { position: absolute; width: 46px; height: 64px; z-index: 2; }

  .search-panel {
    position: absolute; left: 373px; top: 249px; width: 483px; height: 318px;
    background: var(--panel-bg); border: 3px solid var(--plum); border-radius: 12px; z-index: 3;
  }
  .panel-tabs {
    position: absolute; left: 445px; top: 218px; width: 255px; height: 34px;
    background: var(--plum); border-radius: 0 14px 0 0; display: flex; z-index: 3;
    color: var(--white); font-size: 14px; font-weight: 300;
  }
  .panel-tabs span { flex: 1; display: flex; align-items: center; justify-content: center; }
  .panel-tabs .compare { background: var(--plum-soft); border-radius: 0 14px 0 0; }
  .badge {
    position: absolute; left: 372px; top: 173px; width: 110px; height: 110px; border-radius: 50%;
    background: var(--plum); z-index: 4; display: flex; align-items: center; justify-content: center;
  }
  .badge .art { width: 70px; height: 80px; border-radius: 10px; background: linear-gradient(#ffffff, #e9d6e8); }
  .window-controls { position: absolute; right: -14px; top: -18px; display: flex; gap: 6px; }
  .window-controls span {
    width: 22px; height: 22px; border-radius: 50%; background: var(--plum); border: 2px solid var(--white);
    color: var(--white); font-size: 14px; display: flex; align-items: center; justify-content: center; line-height: 1;
  }

  .search-row { position: absolute; left: 16px; top: 50px; display: flex; align-items: center; gap: 12px; }
  .search-row input {
    width: 298px; height: 31px; border: 2px solid var(--plum-soft); background: var(--white);
    font-family: inherit; font-size: 14px; color: #666; padding: 0 8px;
  }

  .results { position: absolute; left: 0; top: 106px; width: 477px; height: 195px; background: var(--card-bg); }
  .result { display: flex; align-items: flex-start; height: 86px; padding: 10px 12px; border-bottom: 1px solid #eee; }
  .result .thumb { width: 68px; height: 64px; background: var(--placeholder); border-radius: 14px; flex: none; }
  .result .text { margin-left: 16px; width: 248px; }
  .result h3 { font-weight: 400; font-size: 16px; color: #444; margin-bottom: 3px; }
  .result p { font-size: 11px; color: var(--muted); line-height: 1.2; }
  .result .stats { margin-left: 18px; font-size: 11px; color: #666; }
  .result .stats div { display: flex; align-items: center; gap: 8px; height: 15px; }
  .result .stats svg { width: 10px; height: 10px; }
  .add-btn {
    margin-top: 6px; display: inline-block; background: var(--orange); color: var(--white); font-size: 11px;
    border-radius: 9px; padding: 2px 9px;
  }
  .scrollbar { position: absolute; right: 8px; top: 8px; width: 3px; height: 110px; background: #bbb; }

  .featured-band {
    position: absolute; left: 0; top: 592px; width: 1200px; height: 208px; background: var(--band); z-index: 1;
    display: flex; padding: 48px 0 0 104px; gap: 26px;
  }
  .featured { width: 92px; text-align: center; color: var(--white); font-size: 16px; }
  .featured .tile { width: 92px; height: 90px; background: #ececec; border-radius: 22px; margin-bottom: 10px; }
</style>
</head>
<body>
  <header class="topbar">
    <nav><a href="#">Home</a><a href="#">Browse</a><a href="#">About</a></nav>
    <span class="divider"></span>
    <form class="login">
      <input class="email" type="text" placeholder="Email">
      <input class="password" type="password" placeholder="Password">
    </form>
    <div class="help"><a href="#">Support</a><a href="#">Contact us</a></div>
  </header>

  <div class="map" role="img" aria-label="Street map of the city with venue locations"></div>

  <svg class="pin" style="left:669px;top:87px" viewBox="0 0 46 64"><path d="M23 63C23 63 2 36 2 22a21 21 0 0 1 42 0c0 14-21 41-21 41z" fill="#8b2487"/><circle cx="23" cy="24" r="9" fill="none" stroke="#fff" stroke-width="3"/><path d="M18 13h10l-5 5z" fill="#fff"/></svg>
  <svg class="pin" style="left:958px;top:266px" viewBox="0 0 46 64"><path d="M23 63C23 63 2 36 2 22a21 21 0 0 1 42 0c0 14-21 41-21 41z" fill="#8b2487"/><circle cx="23" cy="24" r="9" fill="none" stroke="#fff" stroke-width="3"/><path d="M18 13h10l-5 5z" fill="#fff"/></svg>
  <svg class="pin" style="left:268px;top:323px" viewBox="0 0 46 64"><path d="M23 63C23 63 2 36 2 22a21 21 0 0 1 42 0c0 14-21 41-21 41z" fill="#8b2487"/><circle cx="23" cy="24" r="9" fill="none" stroke="#fff" stroke-width="3"/><path d="M18 13h10l-5 5z" fill="#fff"/></svg>
  <svg class="pin" style="left:87px;top:535px" viewBox="0 0 46 64"><path d="M23 63C23 63 2 36 2 22a21 21 0 0 1 42 0c0 14-21 41-21 41z" fill="#8b2487"/><circle cx="23" cy="24" r="9" fill="none" stroke="#fff" stroke-width="3"/><path d="M18 13h10l-5 5z" fill="#fff"/></svg>
  <svg class="pin" style="left:887px;top:527px" viewBox="0 0 46 64"><path d="M23 63C23 63 2 36 2 22a21 21 0 0 1 42 0c0 14-21 41-21 41z" fill="#8b2487"/><circle cx="23" cy="24" r="9" fill="none" stroke="#fff" stroke-width="3"/><path d="M18 13h10l-5 5z" fill="#fff"/></svg>

  <div class="badge"><div class="art" role="img" aria-label="Illustration of a bride and groom"></div></div>
  <div class="panel-tabs"><span class="search">Search</span><span class="compare">Compare</span></div>

  <section class="search-panel">
    <div class="window-controls"><span>&#8211;</span><span>&#215;</span></div>
    <div class="search-row">
      <svg width="20" height="20" viewBox="0 0 20 20"><circle cx="10" cy="10" r="5" fill="none" stroke="#999" stroke-width="1.5"/><circle cx="10" cy="10" r="1.8" fill="#999"/><path d="M10 1v4M10 15v4M1 10h4M15 10h4" stroke="#999" stroke-width="1.5"/></svg>
      <input type="text" value="Harbor City, Street here">
    </div>
    <div class="results">
      <article class="result">
        <div class="thumb"></div>
        <div class="text"><h3>Lorem Ipsum</h3><p>Simply dummy text of the printing and types industry. Lorem Ipsum has been the industry's 1500s, standard dummy text ever since the</p></div>
        <div class="stats">
          <div><svg viewBox="0 0 10 10"><path d="M1 9L5 1l4 8z" fill="#666"/></svg>5.33 &nbsp;km</div>
          <div><svg viewBox="0 0 10 10"><path d="M5 0l1.5 3.3 3.5.4-2.6 2.4.7 3.5L5 7.9 1.9 9.6l.7-3.5L0 3.7l3.5-.4z" fill="#666"/></svg>50 %</div>
          <span class="add-btn">Add to compare</span>
        </div>
      </article>
      <article class="result">
        <div class="thumb"></div>
        <div class="text"><h3>Lorem Ipsum</h3><p>Simply dummy text of the printing and types industry. Lorem Ipsum has been the industry's 1500s, standard dummy text ever since the</p></div>
        <div class="stats">
          <div><svg viewBox="0 0 10 10"><path d="M1 9L5 1l4 8z" fill="#666"/></svg>5.33 &nbsp;km</div>
          <div><svg viewBox="0 0 10 10"><path d="M5 0l1.5 3.3 3.5.4-2.6 2.4.7 3.5L5 7.9 1.9 9.6l.7-3.5L0 3.7l3.5-.4z" fill="#666"/></svg>50 %</div>
          <span class="add-btn">Add to compare</span>
        </div>
      </article>
      <span class="scrollbar"></span>
    </div>
  </section>

  <section class="featured-band">
    <div class="featured"><div class="tile"></div>Lorem Ipsum</div>
    <div class="featured"><div class="tile"></div>Lorem Ipsum</div>
    <div class="featured"><div class="tile"></div>Lorem Ipsum</div>
    <div class="featured"><div class="tile"></div>Lorem Ipsum</div>
  </section>
</body>
</html>
```